Recruitment flyer for Building Inspectors | 4 page A4 color brochure

Coastline Estate & Structure Surveys requires a four page A4 color brochure for new staff who will be joining the organisation.

The brochure is received during the interview for the job role. so we are looking for nice glossy pictures combined with sufficient text to enable the applicant to make an informed decision.

I have attached a word document that may help plus lots of pictures that are on the website that could be used also.

Target Market(s)

New employees of Coastline Estate & Structure Surveys

Industry/Entity Type

Home Inspection

Font styles to use
Sans Serif

Colors
0355a3
3276b5
85abd2

Requirements
Must have
• Professional, full color, combinations of text and background imagery.
Nice to have
• solid footer
Should not have
• happy colors

```html
<!DOCTYPE html>
<html lang="en">
<head>
<meta charset="utf-8">
<title>Coastline Estate &amp; Structure Surveys – Staff Brochure</title>
<link href="https://fonts.googleapis.com/css2?family=Open+Sans:wght@400;600;700&display=swap" rel="stylesheet">
<style>
  :root{
    --brand-deep:#0355a3;
    --brand-mid:#3276b5;
    --brand-soft:#85abd2;
    --brand-pale:#dbe8f5;
    --ink:#222;
    --rule:#c9ced4;
    --stage:#e9ebee;
    --paper:#fff;
  }
  *{box-sizing:border-box;margin:0;padding:0}
  html,body{width:895px;height:1200px;overflow:hidden}
  body{background:var(--stage);font-family:"Open Sans",sans-serif;color:var(--ink);position:relative}
  .spread{position:absolute;display:flex;box-shadow:0 4px 14px rgba(0,0,0,.18)}
  .spread--covers{left:78px;top:40px;width:742px;height:532px}
  .spread--inside{left:78px;top:604px;width:742px;height:540px}
  .page{position:relative;width:371px;height:100%;background:var(--paper);overflow:hidden}
  .photo{position:absolute}
  .curve{position:absolute;left:0;width:100%}
  .skyline{position:absolute;left:0;width:100%;height:30px;
    background:linear-gradient(180deg,rgba(3,85,163,0) 0%,rgba(50,118,181,.55) 45%,var(--brand-mid) 100%)}
  .footer{position:absolute;left:0;bottom:0;width:100%;height:28px;background:var(--brand-deep);
    color:#fff;font-size:8.5px;display:flex;align-items:center;justify-content:center;letter-spacing:.1px}

  /* back cover */
  .back .photo{left:0;top:0;width:371px;height:300px;
    background:linear-gradient(135deg,#5a4536 0%,#8c6f5c 40%,#cfc2b6 70%,#e8e2dc 100%)}
  .back .intro{position:absolute;left:29px;top:362px;width:300px;color:var(--ink)}
  .intro h2{font-size:9.5px;font-weight:700;margin-bottom:4px}
  .intro p{font-size:7.4px;line-height:16px}
  .back .skyline{top:464px}
  .back .footer{height:38px}

  /* front cover */
  .front .masthead{position:absolute;left:0;top:0;width:100%;height:92px;display:flex;align-items:center;justify-content:center}
  .brand-name{font-weight:700;color:var(--brand-deep);font-size:12.5px;line-height:1.25;text-align:left;letter-spacing:.4px}
  .brand-mark{width:14px;height:14px;background:var(--brand-deep);margin-right:9px}
  .front .photo{left:0;top:96px;width:371px;height:258px;
    background:linear-gradient(180deg,#9cc3e8 0%,#d9e6ef 35%,#c9c3b8 60%,#6e8e4d 100%)}
  .front .quote-area{position:absolute;left:0;top:340px;width:100%;height:170px;
    background:linear-gradient(180deg,#cfe0f1 0%,#eaf2fa 50%,#d5e4f3 100%)}
  .front .quote{position:absolute;left:58px;top:388px;width:252px;font-size:7.8px;line-height:16.5px;text-align:justify;color:var(--ink)}
  .front .skyline{top:470px}
  .front .footer{height:32px}

  /* inside pages */
  .story{position:absolute}
  .story h3{font-size:8.5px;font-weight:400;margin-bottom:8px;line-height:12px}
  .story .lines{border-top:1px solid var(--rule)}
  .story .lines span{display:block;height:17px;border-bottom:1px solid var(--rule)}
  .story--tight .lines span{height:15px}
  .inside .skyline{top:468px}
  .inside .footer{height:44px;padding-top:4px}
  .band{position:absolute;left:0;width:100%;background:linear-gradient(180deg,#f4f4f4,#fff 40%,#f6f6f6)}
</style>
</head>
<body>

<section class="spread spread--covers">
  <article class="page back">
    <div class="photo" role="img" aria-label="Photo of a smiling support team member wearing a headset at her desk"></div>
    <svg class="curve" style="top:120px;height:300px" viewBox="0 0 371 300" preserveAspectRatio="none" role="img" aria-label="Soft blue wave decoration sweeping across the page">
      <defs>
        <linearGradient id="waveFill" x1="0" y1="0" x2="1" y2="1">
          <stop offset="0" stop-color="#eef4fb"/>
          <stop offset="1" stop-color="#bcd4ec"/>
        </linearGradient>
      </defs>
      <path d="M0 170 C120 175 230 160 280 90 C310 50 340 20 371 0 L371 252 C200 272 90 232 0 182Z" fill="url(#waveFill)"/>
      <path d="M0 182 C90 232 200 272 371 252 L371 300 L0 300Z" fill="#fff"/>
      <path d="M0 182 C90 232 200 272 371 252" fill="none" stroke="var(--brand-deep)" stroke-width="4"/>
    </svg>
    <div class="intro">
      <h2>Final Text</h2>
      <p>Final Text Final Text Final Text Final Text Final Text Final Text Final Text Final Text Final Text Final Text Final Text Final Text Final Text Final Text Final Text Final Text .</p>
      <p>Final Text Final Text Final Text Final Text Final Text Final Text Final Text Final Text Final Text Final Text Final.</p>
    </div>
    <div class="skyline" role="img" aria-label="Blue city skyline silhouette illustration"></div>
    <footer class="footer">CESS - Coastline Estate &amp; Structure Surveys</footer>
  </article>

  <article class="page front">
    <header class="masthead">
      <span class="brand-mark"></span>
      <span class="brand-name">COASTLINE ESTATE &amp;<br>STRUCTURE SURVEYS</span>
    </header>
    <div class="photo" role="img" aria-label="Photo of a suburban house viewed through a magnifying glass held by a hand"></div>
    <svg class="curve" style="top:0;height:120px" viewBox="0 0 371 120" preserveAspectRatio="none" aria-hidden="true">
      <path d="M0 0 L371 0 L371 3 L0 3Z" fill="var(--brand-deep)"/>
      <path d="M0 72 C110 100 260 108 371 80" fill="none" stroke="var(--brand-deep)" stroke-width="5"/>
      <path d="M0 82 C110 108 260 114 371 88" fill="none" stroke="var(--brand-soft)" stroke-width="1.5"/>
    </svg>
    <div class="quote-area" role="img" aria-label="Soft blue background texture"></div>
    <svg class="curve" style="top:330px;height:40px" viewBox="0 0 371 40" preserveAspectRatio="none" aria-hidden="true">
      <path d="M0 22 C120 8 260 6 371 18" fill="none" stroke="var(--brand-deep)" stroke-width="4"/>
    </svg>
    <p class="quote">Grab your reader’s attention with a great quote from the document or use this space to emphasize a key point. To place this text box anywhere on the page, just drag it.</p>
    <div class="skyline" role="img" aria-label="Blue city skyline silhouette illustration"></div>
    <footer class="footer">CESS - Coastline Estate &amp; Structure Surveys</footer>
  </article>
</section>

<section class="spread spread--inside">
  <article class="page inside inside--left">
    <div class="band" style="top:0;height:168px"></div>
    <div class="story" style="left:14px;top:18px;width:218px">
      <h3>Story 1</h3>
      <div class="lines"><span></span><span></span><span></span><span></span><span></span><span></span><span></span></div>
    </div>
    <div class="photo" style="left:253px;top:0;width:118px;height:168px;background:linear-gradient(180deg,#8f9499,#c5c8cb 50%,#9aa08f)" role="img" aria-label="Photo of a terrace house with iron lace balcony"></div>

    <div class="photo" style="left:0;top:198px;width:128px;height:114px;background:linear-gradient(135deg,#5b5c5e,#8a7766 50%,#4e4f52)" role="img" aria-label="Photo of damaged roof shingles"></div>
    <div class="story" style="left:150px;top:193px;width:212px">
      <h3>Story 2</h3>
      <div class="lines"><span></span><span></span><span></span><span></span><span></span><span></span><span></span></div>
    </div>

    <div class="story story--tight" style="left:14px;top:360px;width:218px">
      <h3>Story 3</h3>
      <div class="lines"><span></span><span></span><span></span><span></span><span></span><span></span></div>
    </div>
    <div class="photo" style="left:253px;top:348px;width:118px;height:150px;background:linear-gradient(180deg,#8a4a35,#b07a5c 50%,#d8c6a8)" role="img" aria-label="Photo of an inspector in a hard hat examining a brick wall"></div>

    <svg class="curve" style="top:150px;height:40px" viewBox="0 0 371 40" preserveAspectRatio="none" aria-hidden="true">
      <path d="M0 10 C120 30 260 32 371 20 L371 40 L0 40Z" fill="#fff"/>
      <path d="M0 10 C120 30 260 32 371 20" fill="none" stroke="var(--brand-mid)" stroke-width="4"/>
    </svg>
    <svg class="curve" style="top:325px;height:40px" viewBox="0 0 371 40" preserveAspectRatio="none" aria-hidden="true">
      <path d="M0 26 C120 10 260 6 371 14" fill="none" stroke="var(--brand-mid)" stroke-width="4"/>
    </svg>
    <div class="skyline" role="img" aria-label="Blue city skyline silhouette illustration"></div>
    <footer class="footer">CESS - Coastline Estate &amp; Structure Surveys</footer>
  </article>

  <article class="page inside inside--right">
    <div class="band" style="top:0;height:168px"></div>
    <div class="photo" style="left:0;top:0;width:115px;height:168px;background:linear-gradient(180deg,#4f8ed0,#a9c6e2 40%,#8a8f7a 70%,#5b7a45)" role="img" aria-label="Photo of a row of terrace houses under blue sky"></div>
    <div class="story" style="left:136px;top:12px;width:222px">
      <h3>Story 4</h3>
      <div class="lines"><span></span><span></span><span></span><span></span><span></span><span></span><span></span><span></span></div>
    </div>

    <div class="story" style="left:12px;top:193px;width:210px">
      <h3>Story 5</h3>
      <div class="lines"><span></span><span></span><span></span><span></span><span></span><span></span><span></span></div>
    </div>
    <div class="photo" style="left:236px;top:198px;width:135px;height:112px;background:linear-gradient(180deg,#c3cdd6,#9aa2a8 45%,#b9c6d2)" role="img" aria-label="Photo of corrugated fibre cement roof sheeting"></div>

    <div class="photo" style="left:0;top:348px;width:115px;height:150px;background:linear-gradient(180deg,#9fb3c4,#6b6a68 40%,#c9d04a 75%,#4a4c50)" role="img" aria-label="Photo of a building inspector in a high-visibility vest"></div>
    <div class="story story--tight" style="left:136px;top:364px;width:222px">
      <h3>Story 6</h3>
      <div class="lines"><span></span><span></span><span></span><span></span><span></span><span></span></div>
    </div>

    <svg class="curve" style="top:150px;height:40px" viewBox="0 0 371 40" preserveAspectRatio="none" aria-hidden="true">
      <path d="M0 22 C120 32 260 28 371 8 L371 40 L0 40Z" fill="#fff"/>
      <path d="M0 22 C120 32 260 28 371 8" fill="none" stroke="var(--brand-mid)" stroke-width="4"/>
    </svg>
    <svg class="curve" style="top:325px;height:40px" viewBox="0 0 371 40" preserveAspectRatio="none" aria-hidden="true">
      <path d="M0 16 C120 6 260 10 371 28" fill="none" stroke="var(--brand-mid)" stroke-width="4"/>
    </svg>
    <div class="skyline" role="img" aria-label="Blue city skyline silhouette illustration"></div>
    <footer class="footer">CESS - Coastline Estate &amp; Structure Surveys</footer>
  </article>
</section>

</body>
</html>
```